Market Research firm needs updated business cards with new logo

We need the logo to be included somewhere on the card (attached). We would also like the phrases "Impartial, Rigorous, Thorough" and "Insight You Can Rely On" somewhere on the card. Front or back. Our colors are hex codes 6075a7, e48d25 and 5a5b5b. Though you are certainly not limited to those shades, whatever you produce should coordinate with them. I have also attached our favicon. Feel free to use it in your design, but please do not use it to replace the full logo.

Contact Information for Business Card

see project description

Font styles to use
Other font styles liked:
• Open Sans

Requirements
Must have
• the logo
• We use Open Sans font

```html
<!DOCTYPE html>
<html lang="en">
<head>
<meta charset="utf-8">
<title>Norvale Research – Business Cards</title>
<link rel="stylesheet" href="https://fonts.googleapis.com/css2?family=Open+Sans:wght@400;600&family=Roboto:wght@400;700&display=swap">
<style>
  :root {
    --blue-deep: #5265a0;
    --blue-light: #7790c2;
    --orange: #e48d25;
    --grey: #5a5b5b;
    --white: #ffffff;
    --backdrop: #d9d9d9;
  }
  * { margin: 0; padding: 0; box-sizing: border-box; }
  html, body { width: 1200px; height: 900px; overflow: hidden; }
  body {
    background: radial-gradient(circle at 50% 45%, #ececec 0%, var(--backdrop) 100%);
    font-family: "Open Sans", sans-serif;
    position: relative;
  }
  .card {
    position: absolute;
    left: 280px;
    width: 640px;
    height: 366px;
    border-radius: 24px;
    overflow: hidden;
    background: radial-gradient(ellipse at 55% 60%, var(--blue-light) 0%, var(--blue-deep) 85%);
    box-shadow: 0 10px 24px rgba(0,0,0,0.22);
    color: var(--white);
  }
  .card--front { top: 60px; }
  .card--back { top: 474px; }
  .band {
    position: absolute;
    left: 0; right: 0;
    top: 36px;
    height: 94px;
    background: var(--white);
  }
  .brand {
    position: absolute;
    display: flex;
    align-items: center;
    gap: 8px;
    color: var(--grey);
    font-family: "Open Sans", sans-serif;
    font-weight: 400;
    font-size: 34px;
    letter-spacing: -0.5px;
    white-space: nowrap;
  }
  .brand__dot {
    width: 20px; height: 20px;
    border-radius: 50%;
    background: var(--orange);
  }
  .card--front .brand { left: 190px; top: 62px; }
  .card--back .brand { left: 190px; top: 68px; }
  .tagline {
    position: absolute;
    left: 0; right: 0;
    top: 134px;
    text-align: center;
    font-size: 17px;
    line-height: 1.25;
    color: var(--white);
  }
  .person {
    position: absolute;
    left: 60px;
    top: 146px;
    font-family: "Roboto", sans-serif;
  }
  .person__name { font-weight: 700; font-size: 26px; letter-spacing: 0.3px; }
  .person__role {
    font-weight: 700; font-size: 15px;
    margin-left: 150px;
    padding-bottom: 8px;
    border-bottom: 2px solid var(--white);
    width: 220px;
    margin-top: 2px;
  }
  .rule {
    position: absolute;
    left: 60px; top: 238px;
    width: 250px; height: 3px;
    background: var(--white);
  }
  .contacts {
    position: absolute;
    left: 60px; top: 258px;
    list-style: none;
    font-size: 13.5px;
    line-height: 21px;
  }
  .contacts li { display: flex; align-items: center; gap: 10px; }
  .contacts svg { width: 13px; height: 13px; fill: var(--white); flex: none; }
  .contacts .caps { text-transform: uppercase; font-size: 12.5px; }
</style>
</head>
<body>

<section class="card card--front" aria-label="Card front">
  <div class="band"></div>
  <div class="brand"><span class="brand__dot"></span>Norvale Research</div>
  <p class="tagline">"Impartial, Rigorous, Thorough"<br>and "Insight You Can Rely On"</p>
</section>

<section class="card card--back" aria-label="Card back">
  <div class="band"></div>
  <div class="brand"><span class="brand__dot"></span>Norvale Research</div>
  <div class="person">
    <h1 class="person__name">MARINA KESTREL</h1>
    <p class="person__role">LIFE COACH</p>
  </div>
  <div class="rule"></div>
  <ul class="contacts">
    <li><svg viewBox="0 0 24 24"><path d="M6.6 10.8a15 15 0 0 0 6.6 6.6l2.2-2.2a1 1 0 0 1 1-.25 11.4 11.4 0 0 0 3.6.6 1 1 0 0 1 1 1V20a1 1 0 0 1-1 1A17 17 0 0 1 3 4a1 1 0 0 1 1-1h3.5a1 1 0 0 1 1 1c0 1.250.2 2.450.6 3.6a1 1 0 0 1-.25 1z"/></svg>555-014-2736</li>
    <li><svg viewBox="0 0 24 24"><path d="M12 2a10 10 0 1 0 0 20 10 10 0 0 0 0-20zm6.9 6h-3a15 15 0 0 0-1.3-3.9A8 8 0 0 1 18.9 8zM12 4c.9 1.2 1.6 2.5 2 4h-4c.4-1.5 1.1-2.8 2-4zM4.3 14a8 8 0 0 1 0-4h3.4a16 16 0 0 0 0 4zm.8 2h3a15 15 0 0 0 1.3 3.9A8 8 0 0 1 5.1 16zm3-8h-3a8 8 0 0 1 4.3-3.9A15 15 0 0 0 8.1 8zM12 20c-.9-1.2-1.6-2.5-2-4h4c-.4 1.5-1.1 2.8-2 4zm2.3-6H9.7a14 14 0 0 1 0-4h4.6a14 14 0 0 1 0 4zm.3 5.9a15 15 0 0 0 1.3-3.9h3a8 8 0 0 1-4.3 3.9zm1.7-5.9a16 16 0 0 0 0-4h3.4a8 8 0 0 1 0 4z"/></svg>www.northgatestudio.com</li>
    <li><svg viewBox="0 0 24 24"><path d="M2 5h20v14H2zm2 2v.5l8 5 8-5V7zm0 2.8V17h16V9.8l-8 5z"/></svg><span class="caps">marina@calmcounselhub.com</span></li>
    <li><svg viewBox="0 0 24 24"><path d="M12 2a7 7 0 0 0-7 7c0 5 7 13 7 13s7-8 7-13a7 7 0 0 0-7-7zm0 9.5A2.5 2.5 0 1 1 12 6.5a2.5 2.5 0 0 1 0 5z"/></svg>1820 Harbor Lane Fairview, MD 20000</li>
  </ul>
</section>

</body>
</html>
```